Upgrade 4 Images - Bid 1, then we can discuss the other 3

We have a four graphics that we use in various presentations and business proposals. We want to upgrade them to make them really pop and match the level of service we provide, without going overboard.

We're open to new ideas, but the general form and content should stay the same.

I'd like to have all four designed by the same person, but I'm assuming this bid will be for 1 of the four, and then the other three can be contracted as additions.

```html
<!DOCTYPE html>
<html lang="en">
<head>
<meta charset="utf-8">
<title>Operating Quadrants</title>
<link href="https://fonts.googleapis.com/css2?family=Outfit:wght@400;500;600;700&display=swap" rel="stylesheet">
<style>
  :root {
    --bg: #f5f5f5;
    --ink: #111111;
    --card: #ffffff;
    --card-line: #ececee;
    --band: #e3e4e8;
    --icon-fill: #e6e7eb;
    --specialist-a: #0fe8d2;
    --specialist-b: #1e8ff0;
    --enterprise-a: #e21fc4;
    --enterprise-b: #6a1fd8;
    --factory-a: #2fb2f5;
    --factory-b: #6a1ec9;
    --adhoc-a: #ffdc3a;
    --adhoc-b: #ff2f8c;
  }
  * { margin: 0; padding: 0; box-sizing: border-box; }
  html, body { width: 1200px; height: 800px; overflow: hidden; background: var(--bg); }
  body { font-family: "Outfit", sans-serif; color: var(--ink); position: relative; }
  .title {
    position: absolute; top: 56px; left: 0; width: 1200px;
    text-align: center; font-size: 36px; font-weight: 600; letter-spacing: 0.2px;
  }
  .subtitle {
    position: absolute; top: 111px; left: 465px; width: 270px; height: 28px;
    background: #ffffff; border-radius: 14px;
    display: flex; align-items: center; justify-content: center;
    font-size: 16px; font-weight: 400;
    box-shadow: 0 2px 6px rgba(0,0,0,0.04);
  }
  .diagram { position: absolute; top: 0; left: 0; width: 1200px; height: 800px; }
  .axis-label { font-family: "Outfit", sans-serif; font-size: 16px; font-weight: 500; fill: var(--ink); }
  .ring-label { font-family: "Outfit", sans-serif; font-size: 20px; font-weight: 700; fill: #ffffff; letter-spacing: 1.5px; }
  .zone-label { font-family: "Outfit", sans-serif; font-size: 23px; font-weight: 600; fill: var(--ink); }
</style>
</head>
<body>
  <h1 class="title">Operating Quadrants</h1>
  <div class="subtitle">Data Processing as a service</div>

  <svg class="diagram" viewBox="0 0 1500 1000" xmlns="http://www.w3.org/2000/svg">
    <defs>
      <linearGradient id="grad-specialist" x1="0" y1="1" x2="1" y2="0">
        <stop offset="0" stop-color="var(--specialist-a)"/><stop offset="1" stop-color="var(--specialist-b)"/>
      </linearGradient>
      <linearGradient id="grad-enterprise" x1="0" y1="0" x2="1" y2="1">
        <stop offset="0" stop-color="var(--enterprise-a)"/><stop offset="1" stop-color="var(--enterprise-b)"/>
      </linearGradient>
      <linearGradient id="grad-factory" x1="1" y1="0" x2="0" y2="1">
        <stop offset="0" stop-color="var(--factory-a)"/><stop offset="1" stop-color="var(--factory-b)"/>
      </linearGradient>
      <linearGradient id="grad-adhoc" x1="0" y1="0" x2="1" y2="1">
        <stop offset="0" stop-color="var(--adhoc-a)"/><stop offset="1" stop-color="var(--adhoc-b)"/>
      </linearGradient>
      <filter id="card-shadow" x="-20%" y="-20%" width="140%" height="140%">
        <feDropShadow dx="4" dy="6" stdDeviation="7" flood-color="#000" flood-opacity="0.12"/>
      </filter>
      <filter id="hub-shadow" x="-30%" y="-30%" width="160%" height="160%">
        <feDropShadow dx="0" dy="4" stdDeviation="6" flood-color="#000" flood-opacity="0.18"/>
      </filter>
      <clipPath id="clip-tl"><rect x="507" y="270" width="216" height="217" rx="24"/></clipPath>
      <clipPath id="clip-tr"><rect x="778" y="270" width="216" height="217" rx="24"/></clipPath>
      <clipPath id="clip-bl"><rect x="507" y="540" width="216" height="215" rx="24"/></clipPath>
      <clipPath id="clip-br"><rect x="778" y="540" width="216" height="215" rx="24"/></clipPath>
      <path id="arc-specialist" d="M628,512 A122,122 0 0 1 750,390"/>
      <path id="arc-enterprise" d="M750,390 A122,122 0 0 1 872,512"/>
      <path id="arc-adhoc" d="M603,512 A147,147 0 0 0 750,659"/>
      <path id="arc-factory" d="M750,659 A147,147 0 0 0 897,512"/>
    </defs>

    <!-- axis arrows -->
    <g class="axes" fill="var(--band)">
      <rect x="730" y="262" width="40" height="506"/>
      <polygon points="750,217 796,265 704,265"/>
      <polygon points="750,810 796,765 704,765"/>
      <rect x="500" y="495" width="500" height="40"/>
      <polygon points="453,515 501,470 501,560"/>
      <polygon points="1047,515 999,470 999,560"/>
    </g>

    <!-- quadrant cards -->
    <g class="cards">
      <g class="card card-specialist">
        <rect x="507" y="270" width="216" height="217" rx="24" fill="var(--card)" filter="url(#card-shadow)"/>
        <rect x="526" y="289" width="178" height="179" rx="18" fill="none" stroke="var(--card-line)" stroke-width="1.5"/>
        <circle cx="507" cy="270" r="50" fill="url(#grad-specialist)" clip-path="url(#clip-tl)"/>
        <rect x="556" y="317" width="56" height="62" rx="8" fill="var(--icon-fill)" role="img" aria-label="Line icon of a head with puzzle pieces"/>
      </g>
      <g class="card card-enterprise">
        <rect x="778" y="270" width="216" height="217" rx="24" fill="var(--card)" filter="url(#card-shadow)"/>
        <rect x="797" y="289" width="178" height="179" rx="18" fill="none" stroke="var(--card-line)" stroke-width="1.5"/>
        <circle cx="994" cy="270" r="50" fill="url(#grad-enterprise)" clip-path="url(#clip-tr)"/>
        <rect x="888" y="319" width="62" height="60" rx="8" fill="var(--icon-fill)" role="img" aria-label="Line icon of a computer monitor with a globe and binary data"/>
      </g>
      <g class="card card-adhoc">
        <rect x="507" y="540" width="216" height="215" rx="24" fill="var(--card)" filter="url(#card-shadow)"/>
        <rect x="526" y="558" width="178" height="178" rx="18" fill="none" stroke="var(--card-line)" stroke-width="1.5"/>
        <circle cx="507" cy="755" r="50" fill="url(#grad-adhoc)" clip-path="url(#clip-bl)"/>
        <rect x="553" y="639" width="63" height="62" rx="8" fill="var(--icon-fill)" role="img" aria-label="Line icon of a person with a magnified chart and a price tag"/>
      </g>
      <g class="card card-factory">
        <rect x="778" y="540" width="216" height="215" rx="24" fill="var(--card)" filter="url(#card-shadow)"/>
        <rect x="797" y="558" width="178" height="178" rx="18" fill="none" stroke="var(--card-line)" stroke-width="1.5"/>
        <circle cx="994" cy="755" r="50" fill="url(#grad-factory)" clip-path="url(#clip-br)"/>
        <rect x="888" y="638" width="62" height="62" rx="8" fill="var(--icon-fill)" role="img" aria-label="Line icon of a person beside a data funnel and gear"/>
      </g>
    </g>

    <!-- coloured ring quarters -->
    <g class="ring">
      <path d="M583,512 A167,167 0 0 1 750,345 L750,407 A105,105 0 0 0 645,512 Z" fill="url(#grad-specialist)"/>
      <path d="M750,345 A167,167 0 0 1 917,512 L855,512 A105,105 0 0 0 750,407 Z" fill="url(#grad-enterprise)"/>
      <path d="M917,512 A167,167 0 0 1 750,679 L750,617 A105,105 0 0 0 855,512 Z" fill="url(#grad-factory)"/>
      <path d="M750,679 A167,167 0 0 1 583,512 L645,512 A105,105 0 0 0 750,617 Z" fill="url(#grad-adhoc)"/>
    </g>
    <g class="ring-gaps" fill="var(--band)">
      <rect x="732" y="340" width="36" height="344"/>
      <rect x="578" y="496" width="344" height="36"/>
    </g>

    <text class="ring-label"><textPath href="#arc-specialist" startOffset="50%" text-anchor="middle">SPECIALIST</textPath></text>
    <text class="ring-label"><textPath href="#arc-enterprise" startOffset="50%" text-anchor="middle">ENTERPRISE</textPath></text>
    <text class="ring-label"><textPath href="#arc-adhoc" startOffset="50%" text-anchor="middle">Ad Hoc</textPath></text>
    <text class="ring-label"><textPath href="#arc-factory" startOffset="50%" text-anchor="middle">FACTORY</textPath></text>

    <!-- axis labels -->
    <text class="axis-label" x="576" y="522" text-anchor="middle">Low Utilization</text>
    <text class="axis-label" x="927" y="522" text-anchor="middle">High Utilization</text>
    <text class="axis-label" transform="translate(756,342) rotate(-90)" text-anchor="middle">High Maturity</text>
    <text class="axis-label" transform="translate(756,687) rotate(-90)" text-anchor="middle">Low Maturity</text>

    <!-- centre hub -->
    <g class="hub">
      <circle cx="750" cy="512" r="105" fill="#e6e6e8"/>
      <circle cx="750" cy="512" r="85" fill="#ffffff" filter="url(#hub-shadow)"/>
      <text class="zone-label" x="750" y="511" text-anchor="middle">Goldilocks</text>
      <text class="zone-label" x="750" y="538" text-anchor="middle">Zone</text>
    </g>
  </svg>
</body>
</html>
```